Logo & Graphic Design for Children's Event

We need help designing the logo and marketing materials for our summer children's event "Star Parade". This program is for children ages 5-10 and should have a bold, fun feel to it. I would like a strong logo that is the primary feature of the design with additional supporting artwork elements that can be used flexibly in a variety of formats and mediums. I would like the design to capture the overall feel of the event. This event will be themed like a TV game show/variety show and should reflect this vibe.

This design will be used for outside marketing and branding and needs to be provided in a vector format. The types of mediums it would be used on is yard signs, banners, door hangers, social media, etc. (Samples of materials from previous events included in the uploaded files to help you get a feel for the quality and tone that we aim for with this event.)

Target Market(s)

Families with children ages 5-10

Industry/Entity Type

Church

Requirements
Must have
• - Strong logo that communicates the feel of the event and includes the name "Star Parade". - Flexible supporting artwork elements that can be used in a variety of mediums. - Must use fonts that are available from free, open sources or can be provided upon delivery of completed project. - Must be kid and family friendly - Event date June 10-14 must be included - Event time 6:30-8:30pm included - Include our church logo attached - Event web address Brightpathmeadow.com/KDC
Nice to have
• - A themed background that could be adapted for use on powerpoint.
Should not have
• - Any content that is scary, violent or not suitable for an audience of children.

```html
<!DOCTYPE html>
<html lang="en">
<head>
<meta charset="utf-8">
<title>Star Parade – Summer Program</title>
<link rel="stylesheet" href="https://fonts.googleapis.com/css2?family=Chewy&family=Cinzel:wght@600&family=Fredoka:wght@500;600&family=Josefin+Sans:wght@600&family=Open+Sans:wght@400&display=swap">
<style>
  :root {
    --paper: #fef1e9;
    --blue: #529ee6;
    --red: #ee2029;
    --yellow: #fdbb12;
    --green: #10c089;
    --pink: #ee6cc6;
    --ink: #231f20;
    --skin: #f8cfb0;
  }
  * { margin: 0; padding: 0; box-sizing: border-box; }
  html, body { width: 847px; height: 1200px; overflow: hidden; background: var(--paper); }
  .poster { position: relative; width: 847px; height: 1200px; background: var(--paper); overflow: hidden; }
  .shapes { position: absolute; inset: 0; }
  .art { position: absolute; }
  .centered { position: absolute; left: 0; width: 847px; text-align: center; }

  .title-top { top: 62px; font-family: "Chewy", cursive; font-size: 136px; line-height: 1; letter-spacing: 4px; padding-left: 28px; }
  .title-top .s { color: var(--blue); }
  .title-top .t { color: var(--red); }
  .title-top .a { color: var(--yellow); }
  .title-top .r { color: var(--green); }
  .title-bottom { top: 207px; font-family: "Cinzel", serif; font-weight: 600; font-size: 72px; line-height: 1; letter-spacing: 10px; color: var(--pink); padding-left: 18px; }
  .program { top: 298px; font-family: "Fredoka", sans-serif; font-weight: 600; font-size: 56px; line-height: 1; color: var(--blue); letter-spacing: 1px; padding-left: 0; }
  .subtitle { top: 364px; font-family: "Open Sans", sans-serif; font-size: 27px; letter-spacing: 9px; color: var(--ink); padding-left: 6px; }

  .date-label { top: 442px; font-family: "Open Sans", sans-serif; font-size: 18px; letter-spacing: 7px; color: var(--ink); padding-left: 0; }
  .date-value { top: 472px; font-family: "Fredoka", sans-serif; font-weight: 600; font-size: 58px; line-height: 1; color: #fff; letter-spacing: 1px; }
  .event-time { top: 580px; font-family: "Josefin Sans", sans-serif; font-weight: 600; font-size: 38px; line-height: 1; color: var(--ink); padding-left: 12px; }
  .tagline { top: 659px; font-family: "Open Sans", sans-serif; font-size: 27px; color: var(--blue); padding-left: 14px; }
  .activities { top: 718px; font-family: "Open Sans", sans-serif; font-size: 18.5px; line-height: 26.5px; color: var(--ink); padding-left: 14px; }

  .price { top: 900px; font-family: "Open Sans", sans-serif; color: #fff; padding-left: 0; }
  .price .adults { display: block; font-size: 48px; line-height: 1; }
  .price .kids { display: block; font-size: 35px; line-height: 1.1; }

  .church { position: absolute; top: 1045px; left: 337px; display: flex; align-items: center; gap: 8px; }
  .church-dot { width: 56px; height: 56px; border-radius: 50%; background: var(--ink); }
  .church-name { font-family: "Josefin Sans", sans-serif; font-weight: 600; font-size: 17px; line-height: 1.05; color: var(--ink); }

  .address { top: 1111px; font-family: "Josefin Sans", sans-serif; font-weight: 600; font-size: 12.5px; color: var(--ink); }
  .contact { top: 1133px; font-family: "Josefin Sans", sans-serif; font-weight: 600; font-size: 12.5px; color: var(--ink); }
  .contact .sep { display: inline-block; margin: 0 12px; }
  .website { top: 1160px; font-family: "Josefin Sans", sans-serif; font-weight: 600; font-size: 21px; color: var(--ink); }
</style>
</head>
<body>
<main class="poster">
  <svg class="shapes" width="847" height="1200" viewBox="0 0 847 1200" aria-hidden="true">
    <path class="blob-top" d="M197 0 H597 C600 30 560 60 480 52 C420 46 380 40 330 60 C270 82 200 70 197 30 Z" fill="var(--blue)"/>
    <circle class="ball-corner" cx="816" cy="10" r="78" fill="var(--red)"/>
    <path class="blob-left" d="M0 220 C30 215 40 250 34 300 C28 360 30 390 48 420 C60 450 40 475 0 479 Z" fill="var(--pink)"/>
    <path class="blob-bottom-left" d="M0 1200 V1140 C30 1110 60 1120 90 1100 C130 1085 165 1120 169 1200 Z" fill="var(--yellow)"/>
    <path class="blob-bottom-right" d="M721 1200 C730 1160 760 1130 795 1134 C815 1140 822 1175 822 1200 Z" fill="var(--green)"/>
    <path class="pill-date" d="M190 425 C320 412 560 418 660 430 C700 440 700 545 650 552 C520 565 320 565 200 555 C130 545 125 432 190 425 Z" fill="var(--yellow)"/>
    <path class="pill-price" d="M300 873 C400 860 520 862 570 880 C610 900 605 1000 560 1020 C470 1035 360 1030 290 1010 C240 990 240 890 300 873 Z" fill="var(--blue)"/>
  </svg>

  <div class="art" role="img" aria-label="Cartoon rocket illustration" style="left:22px;top:39px;width:113px;height:158px;background:linear-gradient(150deg,var(--red),var(--blue) 45%,var(--yellow));border-radius:50% 50% 20% 20%;"></div>
  <div class="art" role="img" aria-label="Music notes illustration" style="left:90px;top:256px;width:48px;height:132px;background:var(--blue);border-radius:24px;opacity:.85;"></div>
  <div class="art" role="img" aria-label="Yellow brush stroke with music notes" style="left:729px;top:127px;width:118px;height:242px;background:linear-gradient(180deg,var(--yellow),var(--blue));border-radius:30px 0 0 30px;"></div>
  <div class="art" role="img" aria-label="Planet earth illustration" style="left:757px;top:391px;width:90px;height:141px;background:linear-gradient(135deg,var(--blue),var(--green));border-radius:70px 0 0 70px;"></div>
  <div class="art" role="img" aria-label="Dancer silhouette" style="left:687px;top:510px;width:82px;height:146px;background:var(--red);border-radius:40px;"></div>
  <div class="art" role="img" aria-label="Green leaf shape" style="left:0;top:515px;width:62px;height:161px;background:var(--green);border-radius:0 40px 40px 0;"></div>
  <div class="art" role="img" aria-label="Treble clef with record and sound bars" style="left:73px;top:529px;width:121px;height:163px;background:var(--pink);border-radius:50%;"></div>
  <div class="art" role="img" aria-label="Cheerful cartoon girl with crown jumping" style="left:0;top:698px;width:225px;height:417px;background:linear-gradient(180deg,var(--yellow),var(--pink) 60%,var(--skin));border-radius:0 110px 60px 0;"></div>
  <div class="art" role="img" aria-label="Cheerful cartoon boy in unicorn hood jumping" style="left:611px;top:681px;width:236px;height:422px;background:linear-gradient(180deg,var(--green),var(--yellow) 40%,var(--blue));border-radius:110px 0 0 80px;"></div>

  <h1>
    <span class="centered title-top"><span class="s">S</span><span class="t">T</span><span class="a">A</span><span class="r">R</span></span>
    <span class="centered title-bottom">PARADE</span>
  </h1>
  <p class="centered program">SUMMER PROGRAM</p>
  <p class="centered subtitle">Creative Activities</p>

  <p class="centered date-label">DATE</p>
  <p class="centered date-value">JUNE 10 TO 14</p>
  <p class="centered event-time">EVENT TIME: 6:30-8:30PM</p>
  <p class="centered tagline">SOMETHING FUN FOR EVERYONE</p>
  <p class="centered activities">ACTIVITIES INCLUDES<br>MUSIC &amp; DANCING - GAMES - FACE PAINTING<br>THRILLING GAMS - LEARNING EXPERIENCES<br>PRIZES AND MUCH, MUCH MORE!</p>

  <p class="centered price"><span class="adults">Adults $5</span><span class="kids">children free</span></p>

  <div class="church">
    <span class="church-dot"></span>
    <span class="church-name">BRIGHTPATH MEADOW<br>CHURCH</span>
  </div>
  <p class="centered address">1450 MEADOW LANE, BRIGHTPATH KS, 66000</p>
  <p class="centered contact">INFO@BRIGHTPATHMEADOW.COM<span class="sep">|</span>555-014-2290</p>
  <p class="centered website">WWW.BRIGHTPATHMEADOW.COM/KDC</p>
</main>
</body>
</html>
```